Consumer facing site as a spin off of primary B2B site

Create a consumer-focused website for a product that transforms TVs into digital frames, based on primary digital signage website https://lumora-view.com.
Requirements
1. Homepage
• Hero Section: Engaging imagery of the product in use in home settings, with a clear, concise value proposition.
• Introduction Video: A short, engaging video that explains the product's key features and benefits.
• Clear Product Value Proposition: "Transform your TVs into shared family albums", "Easily connect with loved ones through photos and videos", etc.
• How It Works: A simple step-by-step guide or infographic showing how easy it is to set up and use.
• Testimonials: Snippets from real users showcasing how the product has enhanced their home and family life.
• Visual appeal: Images of the product in use (families enjoying content, simple setup on TVs)
• Clear Calls to Action: "Try for Free," "Learn More"
2. Product Details Page
• Features Overview: Detailed descriptions of key features, including screen size flexibility, connectivity, social features, and interactivity.
• Simplify Feature Language: Avoid technical jargon, focus on benefits for families (easy sharing, remote management, slideshow options)
• Showcase Scenarios: "Share baby photos with grandparents", "Keep in touch while traveling", "Send video messages for birthdays"
• Technical Specifications: Information on app compatibility, resolution support, storage options, and any hardware requirements.
• Gallery: High-resolution images showing the product's interface, app screenshots, and examples of it being used in various home environments.
3. FAQ & Support
• Frequently Asked Questions: Answers to common queries about setup, compatibility, subscriptions, and troubleshooting.
• Setup Guides and Tutorials: Step-by-step instructions and video tutorials for setting up and personalizing the product.
• Customer Support: Contact form, live chat, and support hotline information for users needing assistance.
4. Pricing & Subscription Plans
• Details on pricing for the app/service, with a comparison chart if multiple tiers are offered.
• Subscription Benefits: A breakdown of what's included in the subscription, such as cloud storage, exclusive features, and any family sharing options.
• Free Trial Offer: Information on how to start a free trial, what it includes, and how users can subscribe afterward.
5. About Us
• Our Story: Background on LumoraView, the team, and the mission behind the product.
• Vision for Families: Explanation of how the product aims to bring families closer together.
• Sustainability and Social Responsibility
Also need a quick UI refresh (Style/Icons) for the companion mobile app. See attached document

```html
<!DOCTYPE html>
<html lang="en">
<head>
<meta charset="utf-8">
<title>LumoraView — Transform your TVs into shared family albums</title>
<link href="https://fonts.googleapis.com/css2?family=Roboto:ital,wght@0,400;0,500;0,700;0,900;1,400&display=swap" rel="stylesheet">
<style>
:root{
  --purple:#6b3fa0;
  --purple-light:#8d67c0;
  --purple-soft:#a68bd0;
  --ink:#222228;
  --grey:#6f6f78;
  --footer:#262628;
  --white:#ffffff;
}
*{box-sizing:border-box;margin:0;padding:0}
html,body{width:1200px;height:2785px;overflow:hidden}
body{position:relative;font-family:'Roboto',sans-serif;color:var(--ink);background:var(--white)}
.abs{position:absolute}

/* Nav */
.site-nav{position:absolute;left:0;top:0;width:1200px;height:61px;background:var(--purple);z-index:5}
.brand{position:absolute;display:flex;align-items:center;gap:9px;color:var(--white);font-weight:700;font-size:24px}
.brand-dot{width:34px;height:34px;border-radius:50%;border:3px solid var(--white)}
.site-nav .brand{left:144px;top:12px}
.nav-links{position:absolute;left:447px;top:20px;display:flex;gap:29px;list-style:none;border-left:2px solid var(--white);padding-left:5px}
.nav-links li{color:var(--white);font-size:15px;font-weight:500}
.nav-search{position:absolute;left:1038px;top:21px}

/* Hero */
.hero{position:absolute;left:0;top:61px;width:1200px;height:540px;overflow:hidden}
.hero-photo{position:absolute;inset:0;background:linear-gradient(90deg,#e9ecf5 0%,#e4e6ee 30%,#b7b2ad 55%,#8c7f74 75%,#6d6a6d 100%)}
.hero h1{position:absolute;left:143px;top:101px;font-size:57px;line-height:62px;font-weight:900;color:#2a2a2e;letter-spacing:-0.5px}
.hero-sub{position:absolute;left:143px;top:245px;font-size:18px;color:#2a2a2e}
.btn{position:absolute;height:51px;border-radius:26px;display:flex;align-items:center;justify-content:center;font-size:14px;font-weight:500;color:var(--white)}
.btn-primary{background:var(--purple)}
.btn-secondary{background:var(--purple-light)}
.btn-white{background:var(--white);color:var(--purple)}
.dots{position:absolute;left:144px;top:401px;display:flex;gap:13px}
.dots span{width:7px;height:7px;border-radius:50%;background:#c8c8d4}
.dots span.on{background:var(--purple)}

/* Intro */
.intro-title{position:absolute;left:0;width:1200px;top:656px;text-align:center;font-size:43px;line-height:47px;font-weight:700}
.intro-title em{font-style:normal;color:var(--purple)}
.intro-text{position:absolute;left:150px;width:900px;top:769px;text-align:center;font-size:15.5px;line-height:25px;color:var(--grey)}
.video{position:absolute;left:220px;top:853px;width:760px;height:362px;border:3px solid var(--white);box-shadow:0 3px 8px rgba(0,0,0,.35);background:linear-gradient(135deg,#6f6a66 0%,#a39a90 35%,#5b5e66 60%,#8e8b86 100%);z-index:2}
.video-label{position:absolute;left:279px;top:184px;background:var(--white);padding:3px 9px;font-size:26px;font-weight:900;color:#1f5a55}
.play{position:absolute;left:356px;top:158px;width:44px;height:44px;border-radius:50%;background:var(--purple);display:flex;align-items:center;justify-content:center}

/* How it works */
.how-title{position:absolute;left:0;width:1200px;top:1276px;text-align:center;font-size:41px;font-weight:700;color:var(--white);z-index:3}
.step-text{position:absolute;text-align:center;color:var(--white);font-size:16px;font-weight:500;line-height:22px;z-index:3;white-space:nowrap}

/* Testimonials */
.testimonial-photo{position:absolute;left:0;top:1838px;width:1200px;height:660px;background:linear-gradient(180deg,#ffffff 0%,#f3f1ef 35%,#d9d1c6 65%,#8c7f72 100%)}
.testi-title{position:absolute;left:0;width:1200px;top:1896px;text-align:center;font-size:41px;font-weight:700}
.avatar{position:absolute;left:160px;top:2004px;width:170px;height:170px;border-radius:50%;border:3px solid var(--purple-light);background:linear-gradient(180deg,#cfcac4,#9c8c78)}
.quote{position:absolute;left:412px;top:2000px;width:680px;font-style:italic;font-size:16.5px;line-height:29.5px;color:#4a4a50;white-space:nowrap}
.quote-mark{position:absolute;font-size:100px;font-weight:900;color:#c9c9cf;line-height:1}
.author{position:absolute;left:412px;top:2099px;font-size:19px;font-weight:700;color:var(--purple)}
.author-role{position:absolute;left:412px;top:2126px;font-size:16px;color:#333}

/* Footer */
.footer-h{position:absolute;top:2556px;font-size:15px;font-weight:500;color:var(--purple-soft)}
.footer-t{position:absolute;font-size:12.5px;line-height:20px;color:var(--white)}
.links{position:absolute;left:714px;top:2585px;list-style:none}
.links li{font-size:12.5px;color:var(--white);height:25.6px}
.newsletter{position:absolute;left:396px;top:2644px;width:238px;height:40px;border-radius:20px;background:var(--white)}
.newsletter span{position:absolute;left:18px;top:11px;font-size:14px;color:#555}
.newsletter b{position:absolute;right:2px;top:2px;width:86px;height:36px;border-radius:18px;background:var(--purple);color:var(--white);font-size:11px;display:flex;align-items:center;justify-content:center}
.social{position:absolute;top:2618px;width:31px;height:31px;border-radius:50%;border:2px solid var(--white)}
.copyright{position:absolute;left:0;width:1200px;top:2741px;text-align:center;font-size:13px;color:var(--white)}
</style>
</head>
<body>

<header class="site-nav">
  <div class="brand"><span class="brand-dot"></span>LumoraView</div>
  <ul class="nav-links">
    <li>Home</li><li>Products</li><li>FAQ &amp; Support</li><li>Pricing &amp; Subscription Plans</li><li>About Us</li>
  </ul>
  <svg class="nav-search" width="16" height="16" viewBox="0 0 16 16"><circle cx="6.5" cy="6.5" r="5" fill="none" stroke="#fff" stroke-width="2.2"/><line x1="10" y1="10" x2="14.5" y2="14.5" stroke="#fff" stroke-width="2.6" stroke-linecap="round"/></svg>
</header>

<section class="hero">
  <div class="hero-photo" role="img" aria-label="Couple on a sofa using a remote to show family photos on a living-room TV"></div>
  <h1>Transform your TVs into<br>shared family albums</h1>
  <p class="hero-sub">Easily connect with loved ones through photos and videos</p>
  <div class="btn btn-primary" style="left:144px;top:300px;width:162px">TRY FOR FREE</div>
  <div class="btn btn-secondary" style="left:312px;top:300px;width:162px">LEARN MORE</div>
  <div class="dots"><span class="on"></span><span></span><span></span></div>
</section>
<svg class="abs" style="left:0;top:520px;z-index:3" width="1200" height="90" viewBox="0 520 1200 90">
  <polygon points="0,540 290,600 0,600" fill="#fff"/>
  <polygon points="905,600 1200,560 1200,600" fill="#fff"/>
  <rect x="0" y="598" width="1200" height="12" fill="#fff"/>
  <polygon points="362,583 600,513 833,583 600,523" fill="var(--purple)"/>
</svg>

<h2 class="intro-title">Your Content. <em>Your Screens.</em><br>Simplified</h2>
<p class="intro-text">Transform the way you exhibit content while saying goodbye to intricate setups and confusion. Enter a world<br>where your promotions, presentations, and messages take the spotlight across numerous screens fluidly.</p>

<div class="video" role="img" aria-label="Introduction video: collage of rooms with wall-mounted TVs showing shared content">
  <div class="video-label">Set Up Easily</div>
  <div class="play"><svg width="18" height="20" viewBox="0 0 18 20"><polygon points="2,1 17,10 2,19" fill="#fff"/></svg></div>
</div>

<svg class="abs" style="left:0;top:1210px;z-index:1" width="1200" height="630" viewBox="0 1210 1200 630">
  <polygon points="0,1270 222,1214 978,1214 1200,1270 1200,1605 600,1805 0,1605" fill="var(--purple)"/>
  <polygon points="178,1674 600,1818 600,1836 182,1678" fill="#4b2a78"/>
  <polygon points="600,1818 1200,1612 1200,1648 600,1836" fill="var(--purple-light)"/>
  <path d="M340 1413 Q420 1365 505 1430" fill="none" stroke="#fff" stroke-width="1.6" stroke-dasharray="2 4" opacity=".8"/>
  <polygon points="498,1424 510,1434 494,1436" fill="#bbb"/>
  <path d="M692 1470 Q760 1530 860 1468" fill="none" stroke="#fff" stroke-width="1.6" stroke-dasharray="2 4" opacity=".8"/>
  <polygon points="852,1465 866,1465 856,1476" fill="#bbb"/>
  <g fill="none" stroke="#fff" stroke-width="3.5">
    <circle cx="275" cy="1443" r="60"/><circle cx="605" cy="1443" r="60"/><circle cx="948" cy="1443" r="60"/>
  </g>
  <g fill="#fff"><circle cx="228" cy="1400" r="5"/><circle cx="578" cy="1400" r="5"/><circle cx="918" cy="1400" r="5"/></g>
  <circle cx="275" cy="1443" r="42" fill="#9a7cc9"/>
  <g font-family="Roboto,sans-serif" font-weight="300" font-size="112" fill="none" stroke="#fff" stroke-width="3">
    <text x="172" y="1482">1</text><text x="512" y="1482">2</text><text x="862" y="1482">3</text>
  </g>
  <rect x="245" y="1423" width="46" height="30" rx="4" fill="#fff"/><rect x="251" y="1429" width="34" height="18" fill="#9a7cc9"/><rect x="262" y="1455" width="12" height="5" fill="#fff"/><rect x="256" y="1460" width="24" height="4" fill="#fff"/>
  <path d="M602 1432 l-10 11 l10 11 M630 1432 l10 11 l-10 11 M620 1428 l-8 30" fill="none" stroke="#fff" stroke-width="5" stroke-linecap="round" stroke-linejoin="round"/>
  <circle cx="974" cy="1433" r="11" fill="#fff"/><path d="M954 1468 q0-20 20-20 q20 0 20 20z" fill="#fff"/>
</svg>
<h2 class="how-title">How It Works</h2>
<p class="step-text" style="left:125px;width:300px;top:1529px">On your phone or computer,<br>go to https://lumora-view.com/verify</p>
<p class="step-text" style="left:500px;width:220px;top:1524px">Enter the code</p>
<p class="step-text" style="left:795px;width:300px;top:1524px">Sign in to your LumoraView<br>account-This page will refresh<br>when completed</p>
<div class="btn btn-white" style="left:436px;top:1619px;width:160px;z-index:3">TRY FOR FREE</div>
<div class="btn btn-secondary" style="left:604px;top:1619px;width:161px;z-index:3">LEARN MORE</div>

<div class="testimonial-photo" role="img" aria-label="Family sitting on a living-room floor cheering at a TV showing shared photos"></div>
<h2 class="testi-title">Testimonials</h2>
<div class="avatar" role="img" aria-label="Portrait of a smiling customer"></div>
<div class="quote-mark" style="left:340px;top:1993px">“</div>
<p class="quote">Sed ut perspiciatis unde omnis iste natus error sit voluptatem accusantium doloremque<br>laudantium, totam rem aperiam, eaque ipsa quae ab illo inventore veritatis et quasi<br>architecto beatae vitae dicta sunt explicabo. Nemo enim ipsam voluptatem quia</p>
<div class="quote-mark" style="left:902px;top:2108px">”</div>
<p class="author">- JOHN DOE</p>
<p class="author-role">Lorem ipsum dolor sit amet</p>
<svg class="abs" style="left:84px;top:2054px" width="22" height="38" viewBox="0 0 22 38"><path d="M19 3 L4 19 L19 35" fill="none" stroke="#666" stroke-width="3"/></svg>
<svg class="abs" style="left:1094px;top:2054px" width="22" height="38" viewBox="0 0 22 38"><path d="M3 3 L18 19 L3 35" fill="none" stroke="#ccc" stroke-width="3"/></svg>

<footer>
<svg class="abs" style="left:0;top:2410px" width="1200" height="375" viewBox="0 2410 1200 375">
  <polygon points="0,2476 297,2425 600,2508 908,2425 1200,2476 1200,2785 0,2785" fill="var(--footer)"/>
  <polygon points="395,2465 600,2518 805,2465 600,2506" fill="var(--purple)"/>
</svg>
<h3 class="footer-h" style="left:145px">CONTACT US</h3>
<svg class="abs" style="left:148px;top:2597px" width="14" height="18" viewBox="0 0 14 18"><path d="M7 0a7 7 0 0 1 7 7c0 5-7 11-7 11S0 12 0 7a7 7 0 0 1 7-7z" fill="#fff"/><circle cx="7" cy="7" r="2.6" fill="var(--footer)"/></svg>
<p class="footer-t" style="left:180px;top:2587px">4820 Maple Ridge Dr, Suite 210<br>Cedar Falls, TX 78612</p>
<svg class="abs" style="left:147px;top:2641px" width="16" height="16" viewBox="0 0 16 16"><path d="M3 1l3 3-2 2c1 2 3 4 5 5l2-2 3 3-2 3C6 15 1 10 1 3z" fill="#fff"/></svg>
<p class="footer-t" style="left:180px;top:2639px">(555) 014-2273</p>
<svg class="abs" style="left:147px;top:2678px" width="17" height="13" viewBox="0 0 17 13"><rect width="17" height="13" rx="1" fill="#fff"/><path d="M0 1l8.5 6L17 1" fill="none" stroke="var(--footer)" stroke-width="1.5"/></svg>
<p class="footer-t" style="left:180px;top:2674px">info@lumora-view.com</p>

<h3 class="footer-h" style="left:395px">SIGN UP FOR NEWSLETTER</h3>
<p class="footer-t" style="left:396px;top:2589px">excepteur sint occaecat cupidatat non proident,<br>sunt in culpa</p>
<div class="newsletter"><span>Enter email</span><b>SUBSCRIBE</b></div>

<h3 class="footer-h" style="left:710px">QUICK LINKS</h3>
<ul class="links"><li>Home</li><li>Products</li><li>FAQ &amp; Support</li><li>Pricing &amp; Subscription Plans</li><li>About Us</li></ul>

<div class="brand" style="left:905px;top:2560px;font-size:23px"><span class="brand-dot"></span>LumoraView</div>
<span class="social" style="left:925px"></span><span class="social" style="left:964px"></span><span class="social" style="left:1003px"></span>

<p class="copyright">Copyright © 2024 LumoraView.All Rights Reserved &nbsp;| &nbsp;Privacy &nbsp;| &nbsp;Terms of Use</p>
</footer>

</body>
</html>
```